Fashion Site

I need a Home Page and one Internal Page (About or Stores you choose) for a Fashion Retailer called VERANO based in Melbourne Australia. Their product range is high end - European brand (i.e. Corvelli, Batrano etc) shoes, handbags and accessories for Women and Men (Customers 75% Women 25% Men). They currently have a site at www.verano-shoes.com.au (My developer will take this design and push it through the rest of the site).

The new design will be clean and modern and reflect the high end brands they sell. The finished site will have the home page plus the following pages - About - Stores - News/Sales - E-Shop - Contact with links to Join our mail list - Chatterly - Pixelane. I would like a main banner/slider at the top that will have 6 sliding images - through these images I would like to reinforce the following - the products are imported direct from Italy and are the latest most current designs from leading fashion houses (women and men) - A Modern Look with an Italian feel. Then we would also like to show some products/specials from the new E-Shop on the home page as well as the usual links etc.

Their colours are black and white but I am open to having a splash of colour and a must is to use the photography supplied in a creative way (see http://dunestrive.com as an Idea), we want to show that the products are high end - hand made. Their end/tag line is Ever Poised. We DO NOT want any brand names mentioned/Listed (if on a photo that is fine). The site will need to be easy to navigate and google friendly so please keep this in mind with the design. The images supplied include: Product Shots, Melbourne Stores, Italy Warehouse (2 story building with red roof) and Italy Factories/Craftsmen.

Target Market(s)

Fashion Conscious Women and Men who like the finer things in life

Industry/Entity Type

Fashion

Font styles to use
Serif
Sans Serif

Requirements
Must have
• Top Banner with 6 Images that Slide/Scroll in a banner.
Nice to have
• See the Following Sites that may inspire:
https://www.koti.com.au
http://www.fennicraft.co (the Look not the colours)
http://www.tobsandyou.com
Also Like the banner in this http://dunestrive.com (Just the banner)

```html
<!DOCTYPE html>
<html lang="en">
<head>
<meta charset="utf-8">
<title>VERANO — Ever Poised</title>
<link rel="stylesheet" href="https://fonts.googleapis.com/css2?family=Didact+Gothic&display=swap">
<style>
:root{
  --ink:#1f1d1d;
  --topbar:#1a1919;
  --header:#262424;
  --footer:#262424;
  --legal:#1a1919;
  --nav:#bdbdbd;
  --gold:#f2b515;
  --white:#ffffff;
  --paper:#ececec;
  --muted:#8d8d8d;
  --line:#6a6868;
  --sale:#d64545;
  --green:#8ab83a;
  --amber:#e0a80f;
  --teal:#3dbfc4;
  --arrow:#6b6a6a;
}
*{box-sizing:border-box;margin:0;padding:0}
html,body{width:1129px;height:1200px;overflow:hidden}
body{font-family:"Didact Gothic",sans-serif;color:var(--ink);background:var(--white);position:relative}
a{color:inherit;text-decoration:none}
ul{list-style:none}

.topbar{position:absolute;top:0;left:0;width:1129px;height:33px;background:var(--topbar);border-bottom:1px solid #3a3838}
.topbar__note{position:absolute;left:161px;top:11px;font-size:10px;color:#9c9c9c}
.social{position:absolute;display:flex;gap:3px}
.social span{width:14px;height:14px;border-radius:50%;background:#bdbdbd;display:block}
.topbar .social{left:760px;top:10px}
.search{position:absolute;left:825px;top:7px;width:141px;height:20px;background:#2f2d2d;font-size:9px;color:#8a8a8a;padding:5px 5px}
.search svg{position:absolute;right:6px;top:5px}

.header{position:absolute;top:34px;left:0;width:1129px;height:84px;background:var(--header)}
.brand{position:absolute;left:161px;top:30px;display:flex;align-items:baseline;gap:10px}
.brand__name{font-size:30px;color:var(--white);letter-spacing:1px}
.brand__tag{font-size:24px;color:var(--gold)}
.nav{position:absolute;top:40px;left:526px;display:flex;gap:0}
.nav a{font-size:12px;color:var(--nav);width:77px}
.nav a:nth-child(5){width:79px}

.hero{position:absolute;top:118px;left:0;width:1129px;height:322px;background:radial-gradient(ellipse at 35% 40%,#7b7368 0%,#55504a 45%,#3d3a38 100%)}
.hero__photo{position:absolute;inset:0;background:linear-gradient(90deg,rgba(150,40,35,.45) 0%,rgba(0,0,0,0) 18%,rgba(0,0,0,0) 55%,rgba(160,45,35,.5) 80%,rgba(0,0,0,0) 100%)}
.hero__tag{position:absolute;left:720px;top:252px;font-size:29px;color:#e6e6e6}
.dots{position:absolute;left:170px;top:269px;display:flex;gap:7px}
.dots span{width:10px;height:10px;border-radius:50%;background:#e3e3e3}
.dots span:nth-child(2){background:#3b3939}

.offers{position:absolute;top:469px;left:161px;display:flex;gap:16px}
.offer{position:relative;width:259px;height:159px;background:linear-gradient(160deg,#f6f5fa,#e0dde9);box-shadow:0 1px 3px rgba(0,0,0,.25);overflow:hidden}
.offer__image{position:absolute;left:0;top:40px;width:170px;height:90px}
.offer--shoes .offer__image{background:linear-gradient(170deg,#a7c94a,#5d7d1e)}
.offer--bags .offer__image{left:0;top:15px;width:150px;height:115px;background:linear-gradient(180deg,#c8c8c8,#8e8a86)}
.offer--acc .offer__image{left:0;top:50px;width:190px;height:80px;background:linear-gradient(90deg,#f58fb8,#7fd6d8,#f06aa8)}
.offer__title{position:absolute;right:18px;top:26px;text-align:right;font-size:18px;line-height:23px;color:#2a2828}
.badge{position:absolute;width:52px;height:52px;border-radius:50%;color:var(--white);text-align:center;font-size:15px;line-height:14px;padding-top:13px}
.badge small{display:block;font-size:11px}
.offer--shoes .badge{left:26px;top:47px;background:var(--green)}
.offer--bags .badge{left:138px;top:68px;background:var(--amber)}
.offer--acc .badge{left:41px;top:17px;background:var(--teal)}
.offer__bar{position:absolute;left:0;bottom:0;width:100%;height:30px;background:rgba(30,28,28,.88);color:var(--white);display:flex;justify-content:space-between;align-items:center;padding:0 14px;font-size:12px}
.offer__bar em{font-style:normal;font-size:11px}

.products{position:absolute;top:657px;left:0;width:1129px;height:330px;background:var(--paper)}
.products__title{position:absolute;top:27px;width:100%;text-align:center;font-size:15px;color:#6a6868}
.slider-arrow{position:absolute;top:65px;width:32px;height:190px;background:var(--arrow);display:flex;align-items:center;justify-content:center}
.slider-arrow--prev{left:161px}
.slider-arrow--next{left:934px}
.product{position:absolute;top:65px;width:166px}
.product__image{height:190px;background:var(--white);position:relative}
.product__image i{position:absolute;left:28px;top:55px;width:110px;height:80px;border-radius:40%}
.product__meta{display:flex;justify-content:space-between;margin-top:7px;font-size:7px;color:#888}
.product__meta b{font-weight:normal;color:#999;letter-spacing:1px}
.product__info{display:flex;justify-content:space-between;margin-top:4px;font-size:9px;color:var(--muted);line-height:12px}
.product__info p{width:100px}
.price{text-align:right;color:#333;font-size:10px}
.price s{display:block;color:var(--sale);font-size:9px}

.footer{position:absolute;top:987px;left:0;width:1129px;height:178px;background:var(--footer);color:#d8d8d8}
.footer__col{position:absolute;top:15px;width:127px}
.footer__col h3{font-weight:normal;font-size:11px;margin-bottom:9px}
.footer__col li{font-size:8px;border-bottom:1px solid var(--line);padding:3px 0 4px}
.newsletter{position:absolute;left:728px;top:15px;width:239px}
.newsletter h3{font-weight:normal;font-size:11px;margin-bottom:9px}
.newsletter__field{height:25px;background:#3a3838;display:flex;align-items:center;gap:4px;padding-left:2px;position:relative}
.newsletter__field span{width:26px;height:17px;background:#d9d9d9}
.newsletter__field svg{position:absolute;right:10px;top:8px}
.newsletter p{font-size:8px;line-height:12px;margin-top:10px}
.newsletter h4{font-weight:normal;font-size:10px;margin-top:22px}

.legal{position:absolute;top:1165px;left:0;width:1129px;height:35px;background:var(--legal);color:#cfcfcf;font-size:8px}
.legal__copy{position:absolute;left:161px;top:14px}
.legal__social{position:absolute;left:844px;top:14px}
.legal .social{left:917px;top:10px}
</style>
</head>
<body>

<div class="topbar">
  <span class="topbar__note">100% GENUINE BRANDS</span>
  <div class="social"><span></span><span></span><span></span></div>
  <div class="search">SEARCH
    <svg width="10" height="10" viewBox="0 0 10 10"><circle cx="4" cy="4" r="3" fill="none" stroke="#8a8a8a" stroke-width="1.2"/><line x1="6.2" y1="6.2" x2="9" y2="9" stroke="#8a8a8a" stroke-width="1.2"/></svg>
  </div>
</div>

<header class="header">
  <a class="brand" href="#"><span class="brand__name">VERANO</span><span class="brand__tag">Ever Poised</span></a>
  <nav class="nav">
    <a href="#">Home</a><a href="#">About</a><a href="#">Stores</a><a href="#">News/Sales</a><a href="#">E-Shop</a><a href="#">Contact</a>
  </nav>
</header>

<section class="hero" role="img" aria-label="Slide photo of a handmade leather shoe beside red bougainvillea flowers">
  <div class="hero__photo"></div>
  <div class="hero__tag">Ever Poised</div>
  <div class="dots"><span></span><span></span><span></span><span></span><span></span><span></span></div>
</section>

<section class="offers">
  <a class="offer offer--shoes" href="#">
    <div class="offer__image" role="img" aria-label="Green leather heel shoe"></div>
    <h2 class="offer__title" style="font-weight:normal">ELEGANT HEEL<br>SHOES</h2>
    <div class="badge">25%<small>OFF</small></div>
    <div class="offer__bar"><span>Heel Shoes</span><em>from $15 &gt;&gt;</em></div>
  </a>
  <a class="offer offer--bags" href="#">
    <div class="offer__image" role="img" aria-label="Silver croc-textured handbag"></div>
    <h2 class="offer__title" style="font-weight:normal">FEMALE<br>HANDBAGS</h2>
    <div class="badge">50%<small>OFF</small></div>
    <div class="offer__bar"><span>Hand Bags</span><em>from $15 &gt;&gt;</em></div>
  </a>
  <a class="offer offer--acc" href="#">
    <div class="offer__image" role="img" aria-label="Pink and turquoise hair bows"></div>
    <h2 class="offer__title" style="font-weight:normal">FEMALE<br>ACCESSORIES</h2>
    <div class="badge">30%<small>OFF</small></div>
    <div class="offer__bar"><span>Female Acessories</span><em>from $15 &gt;&gt;</em></div>
  </a>
</section>

<section class="products">
  <h2 class="products__title" style="font-weight:normal">SHOES AND ACCESSORIES</h2>
  <a class="slider-arrow slider-arrow--prev" href="#"><svg width="8" height="12" viewBox="0 0 8 12"><polyline points="6,1 1,6 6,11" fill="none" stroke="#fff" stroke-width="2"/></svg></a>
  <a class="slider-arrow slider-arrow--next" href="#"><svg width="8" height="12" viewBox="0 0 8 12"><polyline points="2,1 7,6 2,11" fill="none" stroke="#fff" stroke-width="2"/></svg></a>

  <article class="product" style="left:209px">
    <div class="product__image"><i role="img" aria-label="Black flat shoe with polka dot bow" style="background:linear-gradient(160deg,#444,#111)"></i></div>
    <div class="product__meta"><b>★★★★★</b><span>●●</span></div>
    <div class="product__info"><p>Lorem ipsum dolor si amet</p><div class="price">$150.00<s>$190.00</s></div></div>
  </article>
  <article class="product" style="left:391px">
    <div class="product__image"><i role="img" aria-label="Blue leather tote bag" style="background:linear-gradient(160deg,#3a7fd6,#1e4e9c)"></i></div>
    <div class="product__meta"><b>★★★★★</b><span>●●</span></div>
    <div class="product__info"><p>Lorem ipsum dolor si amet</p><div class="price">$150.00<s>$190.00</s></div></div>
  </article>
  <article class="product" style="left:572px">
    <div class="product__image"><i role="img" aria-label="Gold ring with crystal stone" style="background:linear-gradient(160deg,#f0db8a,#c99f3a);height:55px;top:68px"></i></div>
    <div class="product__meta"><b>★★★★★</b><span>●●</span></div>
    <div class="product__info"><p>Lorem ipsum dolor si amet</p><div class="price">$150.00<s>$190.00</s></div></div>
  </article>
  <article class="product" style="left:753px">
    <div class="product__image"><i role="img" aria-label="Black men's leather loafer" style="background:linear-gradient(160deg,#3a3a3a,#0d0d0d)"></i></div>
    <div class="product__meta"><b>★★★★★</b><span>●●</span></div>
    <div class="product__info"><p>Lorem ipsum dolor si amet</p><div class="price">$150.00<s>$190.00</s></div></div>
  </article>
</section>

<footer class="footer">
  <div class="footer__col" style="left:161px"><h3>WOMENS</h3>
    <ul><li>DENIM</li><li>TOPS</li><li>DRESSES</li><li>JACKETS &amp; COATS</li><li>KNITWEAR</li><li>PANTS</li><li>SKIRTS</li></ul></div>
  <div class="footer__col" style="left:346px"><h3>MENS</h3>
    <ul><li>DENIM</li><li>TOPS</li><li>DRESSES</li><li>JACKETS &amp; COATS</li><li>KNITWEAR</li><li>PANTS</li></ul></div>
  <div class="footer__col" style="left:529px"><h3>ACCESSORIES</h3>
    <ul><li>BAGS</li><li>BELTS</li><li>HATS</li><li>JEWELLERY</li><li>WALLETS</li><li>SCARVES</li><li>SHOES</li></ul></div>
  <div class="newsletter"><h3>NEWSLETTER</h3>
    <div class="newsletter__field"><span></span><span></span><span></span><span></span><span></span>
      <svg width="6" height="10" viewBox="0 0 6 10"><polyline points="1,1 5,5 1,9" fill="none" stroke="#aaa" stroke-width="1.3"/></svg></div>
    <p>Lorem ipsum dolor sit amet , Lorem ipsum dolor sit amet ,<br>dolor sit amet , Lorem ipsum dolor sit amet ,</p>
    <h4>ACCEPTED PAYMEN METHODS</h4>
  </div>
</footer>

<div class="legal">
  <span class="legal__copy">© Copyright 2013-2014 Verano . All Rights Reserved.</span>
  <span class="legal__social">Let's Socialize:</span>
  <div class="social"><span></span><span></span><span></span></div>
</div>

</body>
</html>
```